Professional business cards for real estate development company

I need business cards for my new real estate development company. The company, "KORVA" is a real estate development, investment, and advisory firm with a focus on multifamily, office, and mixed-use projects across primary and secondary markets in the Southeast United States.

Style preference is modern

Industry/Entity Type

Real Estate Development

Contact Information for Business Card

The business cards need to include:
Name
Title
Mailing Address
Phone Number
Web Address

Logo is attached. I would like white to be the primary color with incorporation of the company colors: #232D3A and #B5A451

Font styles to use
Other font styles liked:
• Montserrat, Avenir

Requirements
Must have
• Company Logo. No need to include the company name since the name is in the logo.
Should not have
• No line type designs

```html
<!DOCTYPE html>
<html lang="en">
<head>
<meta charset="utf-8">
<title>KORVA Business Cards</title>
<link rel="stylesheet" href="https://fonts.googleapis.com/css2?family=Open+Sans:wght@500&display=swap">
<style>
  :root {
    --navy: #232D3A;
    --navy-soft: #343D48;
    --gold: #B5A451;
    --paper: #FFFFFF;
    --frame: #1A1A1A;
  }
  html, body {
    margin: 0;
    padding: 0;
    width: 1200px;
    height: 1001px;
    overflow: hidden;
    background: var(--paper);
  }
  .sheet {
    display: block;
    width: 1200px;
    height: 1001px;
  }
  .sheet-frame { fill: var(--paper); stroke: var(--frame); stroke-width: 2; }
  .card-base { fill: var(--paper); }
  .band-navy { fill: var(--navy); }
  .ribbon-gold { fill: var(--gold); }
  .brand-name {
    font-family: "Open Sans", sans-serif;
    font-weight: 500;
    fill: var(--navy-soft);
  }
  .contact-badge { fill: var(--navy); }
  .contact-icon { fill: none; stroke: var(--paper); stroke-width: 1.6; stroke-linecap: round; stroke-linejoin: round; }
  .contact-icon-fill { fill: var(--paper); }
</style>
</head>
<body>
<svg class="sheet" viewBox="0 0 1421 1184" xmlns="http://www.w3.org/2000/svg" aria-label="Front and back of the KORVA business card">
  <rect class="sheet-frame" x="2" y="2" width="1417" height="1180"/>

  <!-- Front of card -->
  <g class="card card-front">
    <rect class="card-base" x="338" y="67" width="745" height="496"/>
    <path class="ribbon-gold" d="M338 67 L417 67 L482 397 Q500 460 555 467 Q490 462 460 395 Z"/>
    <path class="band-navy" d="M338 250 L462 428 Q490 467 555 467 L1083 467 L1083 563 L338 563 Z"/>
    <text class="brand-name" x="660" y="348" font-size="112" letter-spacing="4">KORVA</text>
  </g>

  <!-- Back of card -->
  <g class="card card-back">
    <rect class="card-base" x="338" y="621" width="745" height="496"/>
    <path class="ribbon-gold" d="M1083 621 L1004 621 L939 951 Q921 1014 866 1021 Q931 1016 961 949 Z"/>
    <path class="band-navy" d="M1083 804 L959 982 Q931 1021 866 1021 L338 1021 L338 1117 L1083 1117 Z"/>
    <text class="brand-name" x="388" y="777" font-size="64" letter-spacing="2">KORVA</text>

    <g class="contact-list">
      <g class="contact-item contact-email">
        <circle class="contact-badge" cx="390" cy="860" r="23.5"/>
        <rect class="contact-icon" x="383" y="855" width="15" height="10" rx="1"/>
        <path class="contact-icon" d="M383 855 L390.5 861 L398 855"/>
      </g>
      <g class="contact-item contact-phone">
        <circle class="contact-badge" cx="390" cy="921" r="23.5"/>
        <path class="contact-icon-fill" d="M385 914 q2 -1 3 1 l1 2.5 q0.5 1.5 -1 2 q1 3 4 4.5 q0.8 -1.4 2.2 -0.8 l2.4 1.2 q1.6 1 0.4 2.8 q-1.6 2 -4 1.2 q-5 -2 -8 -7.5 q-1.8 -4 0 -6.9 Z"/>
      </g>
      <g class="contact-item contact-web">
        <circle class="contact-badge" cx="391" cy="983" r="23.5"/>
        <circle class="contact-icon" cx="391" cy="983" r="7.5"/>
        <ellipse class="contact-icon" cx="391" cy="983" rx="3.2" ry="7.5"/>
        <path class="contact-icon" d="M383.5 983 H398.5 M385 979 H397 M385 987 H397"/>
      </g>
    </g>
  </g>
</svg>
</body>
</html>
```